Postcard Design

I am in real estate, I wish to design a "farming" tool.

I want to show a sampling of houses (files attached) with the following text:

The spring market is here and the buyers are waiting for YOU!
Order a Value Glance to see what homes in your neighborhood are selling for, or call today for a personal market analysis.

Order your report at: www.48213HouseDeals.net
or reach out to me directly:
Dana Holloway
www.SettleinBrexham.net
555.214.7860
YourRealtorDana@Maildrop.net

I also attached multiple files containing logos - in multiple formats and in black or white, depending on what is easier to use.

Target Market(s)

By neighborhood. I have a list.

Industry/Entity Type

Real Estate

Requirements
Must have
• See description above

```html
<!DOCTYPE html>
<html lang="en">
<head>
<meta charset="utf-8">
<title>Spring Market Postcard – Dana Holloway</title>
<link rel="stylesheet" href="https://fonts.googleapis.com/css2?family=Josefin+Slab:wght@400;600;700&display=swap">
<style>
  :root {
    --ink: #0c0c0c;
    --paper: #ffffff;
    --panel-grey: #9b9b9b;
    --frame-grey: #8a8a8a;
    --soft-text: #d6d6d6;
    --sky: #c9d9e8;
    --lawn: #6f8f4e;
    --siding: #b9b3a6;
  }
  * { box-sizing: border-box; margin: 0; padding: 0; }
  html, body { width: 1200px; height: 1001px; overflow: hidden; background: var(--paper); }
  body { font-family: "Josefin Slab", serif; }

  .sheet {
    position: relative;
    width: 1200px;
    height: 1001px;
    border: 2px solid var(--frame-grey);
    overflow: hidden;
  }

  .panel { position: absolute; }
  .panel--front-art { left: 0; top: 0; width: 644px; height: 500px; background: var(--ink); color: var(--paper); }
  .panel--front-label { left: 644px; top: 0; width: 556px; height: 500px; background: var(--panel-grey); }
  .panel--back-label { left: 0; top: 500px; width: 552px; height: 501px; background: var(--panel-grey); }
  .panel--back-art { left: 552px; top: 500px; width: 648px; height: 501px; background: var(--paper); color: var(--ink); }

  .side-label {
    position: absolute;
    inset: 0;
    display: flex;
    align-items: center;
    justify-content: center;
    font-size: 84px;
    font-weight: 400;
    color: var(--ink);
  }

  .headline {
    position: absolute;
    left: 28px; top: 18px;
    font-size: 27px;
    line-height: 38px;
    font-weight: 400;
  }

  .pitch {
    position: absolute;
    left: 0; top: 140px;
    width: 620px;
    font-size: 19.5px;
    line-height: 25px;
    color: var(--soft-text);
  }
  .pitch span { display: block; white-space: nowrap; }
  .pitch span:nth-child(1), .pitch span:nth-child(2) { padding-left: 62px; }
  .pitch span:nth-child(3) { padding-left: 139px; }
  .pitch span:nth-child(4) { padding-left: 303px; }

  .rule { position: absolute; background: var(--paper); }
  .rule--right { left: 605px; top: 62px; width: 3px; height: 132px; }
  .rule--left { left: 29px; top: 158px; width: 3px; height: 38px; }
  .rule--bottom { left: 347px; top: 461px; width: 260px; height: 3px; }

  .snapshot {
    position: absolute;
    background: var(--paper);
    padding: 12px;
    box-shadow: 0 2px 6px rgba(0,0,0,.5);
  }
  .snapshot__photo {
    width: 100%; height: 100%;
    background: linear-gradient(180deg, var(--sky) 0%, var(--sky) 38%, var(--siding) 38%, #9c9488 72%, var(--lawn) 72%, #56703b 100%);
  }
  .snapshot--one { left: 350px; top: 22px; width: 228px; height: 150px; transform: rotate(-2deg); }
  .snapshot--two { left: 50px; top: 232px; width: 226px; height: 166px; transform: rotate(3deg); }
  .snapshot--three { left: 348px; top: 256px; width: 232px; height: 170px; transform: rotate(-3.5deg); }

  .agent-mark {
    position: absolute;
    left: 22px; top: 404px;
    display: flex;
    align-items: center;
    gap: 16px;
    color: var(--paper);
    font-weight: 400;
  }
  .agent-mark__square { width: 66px; height: 66px; border: 3px solid var(--paper); }
  .agent-mark__name { font-size: 30px; line-height: 32px; }
  .agent-mark__firm { font-size: 13px; letter-spacing: 2px; text-transform: uppercase; }

  .order { position: absolute; left: 22px; top: 16px; }
  .order__line { font-size: 30px; line-height: 43px; font-weight: 400; }
  .order__url { font-size: 31px; line-height: 43px; font-weight: 700; }
  .contact { position: absolute; left: 22px; top: 144px; font-size: 21px; line-height: 30.5px; font-style: normal; }

  .ink-rule { position: absolute; background: var(--ink); }
  .ink-rule--vertical { left: 29px; top: 280px; width: 3px; height: 192px; }
  .ink-rule--foot { left: 40px; top: 471px; width: 35px; height: 3px; }

  .framed-home {
    position: absolute;
    left: 82px; top: 274px;
    width: 193px; height: 127px;
    border: 6px solid var(--ink);
    padding: 6px;
    background: var(--paper);
    transform: rotate(1deg);
  }
</style>
</head>
<body>
<main class="sheet">
  <section class="panel panel--front-art" aria-label="Postcard front">
    <h1 class="headline">The spring market is here<br>and the buyers are<br>waiting for YOU!</h1>

    <div class="snapshot snapshot--one"><div class="snapshot__photo" role="img" aria-label="Two-storey suburban house with garage and green lawn"></div></div>

    <p class="pitch">
      <span>Order a Value Glance</span>
      <span>to see what homes in your</span>
      <span>neighborhood are selling for, or call today for</span>
      <span>a personal market analysis.</span>
    </p>

    <div class="rule rule--right"></div>
    <div class="rule rule--left"></div>

    <div class="snapshot snapshot--two"><div class="snapshot__photo" role="img" aria-label="Colonial brick-and-siding house with bare winter trees"></div></div>
    <div class="snapshot snapshot--three"><div class="snapshot__photo" role="img" aria-label="Light blue townhouse with garage and front shrubs"></div></div>

    <div class="rule rule--bottom"></div>

    <div class="agent-mark">
      <div class="agent-mark__square"></div>
      <div>
        <div class="agent-mark__name">Dana Holloway</div>
        <div class="agent-mark__firm">Brookmere Real Estate</div>
      </div>
    </div>
  </section>

  <section class="panel panel--front-label"><p class="side-label">Front</p></section>
  <section class="panel panel--back-label"><p class="side-label">Back</p></section>

  <section class="panel panel--back-art" aria-label="Postcard back">
    <div class="order">
      <p class="order__line">Order your report at:</p>
      <p class="order__url">www.48213HouseDeals.net</p>
      <p class="order__line">or reach out to me directly:</p>
    </div>
    <address class="contact">
      Dana Holloway<br>
      www.SettleinBrexham.net<br>
      555.214.7860<br>
      YourRealtorDana@Maildrop.net
    </address>

    <div class="ink-rule ink-rule--vertical"></div>
    <div class="ink-rule ink-rule--foot"></div>

    <div class="framed-home"><div class="snapshot__photo" role="img" aria-label="Two-storey colonial house with garage"></div></div>
  </section>
</main>
</body>
</html>
```